BrXpertz Business Cards for SME Experts

We need a business card for a new company based in Clearwater FL called Kestrel of Merit. KoM is your access to on-demand subject matter experts. The final design should be very clean communicating innovation and expertise. Our logo design is attached.

The Information Age has affected the workforce in that automation and computerization have resulted in higher productivity coupled with net job loss of many knowledgeable employees. Combined with the creation of the internet and search capabilities, the disintermediation of the value chain of Subject Matter Experts (SME) has happened. We no longer need to work through traditional consulting firms for all consulting needs, instead the direct access to the SME, through a leaner and lower cost model is what the market is demanding.
BrXpertz is a new marketplace to buy consulting services. The business model is that all consultants (subject matter experts) can become a consulting resource in the marketplace following our guidelines. The consumer can now easily access consultants that they could not find easily before.
In much the way an Zyla car can be identified and requested, so can a BrXpertz Consultant. Each consultant can be identified by: location, expertise, billing rate, and prior experience rating.
By seamlessly connecting consultants to requesters through a new Kestrel of Merit marketplace, you now will have an easy to use and quicker turnaround to request and staff your consulting needs. Leveraging the KoM app, you can access the subject matter expert you need for your business requirement.

Target Market(s)

Small and medium sized companies; non-profits

Industry/Entity Type

Business Consultant

Contact Information for Business Card

Name
website
email address
Logo
mailing address (debating if I really need...)
twitter
LinkedIn

Requirements
Must have
• the logo I have included in the design; want the colors to be consistent with the logo design

```html
<!DOCTYPE html>
<html lang="en">
<head>
<meta charset="utf-8">
<title>Kestrel of Merit – Business Card</title>
<link href="https://fonts.googleapis.com/css2?family=Questrial&family=Montserrat:wght@700&display=swap" rel="stylesheet">
<style>
  :root{
    --bg:#1c1c1e;
    --paper:#f4f4f4;
    --navy:#141a5c;
    --navy-deep:#10164f;
    --teal:#0f8fb5;
    --grey-text:#3a3a3a;
    --rule:#d4d4d4;
    --white:#ffffff;
  }
  *{margin:0;padding:0;box-sizing:border-box}
  html,body{width:1200px;height:1001px;overflow:hidden;background:var(--bg)}
  .canvas{position:relative;width:1200px;height:1001px}
  .card{position:absolute;left:307px;width:586px;height:328px;border-radius:14px;overflow:hidden}
  .card--front{top:134px;background:var(--paper)}
  .card--back{top:541px;background:linear-gradient(180deg,var(--navy) 0%,var(--navy-deep) 100%)}

  .logo-mark{position:absolute;width:96px;height:96px;border-radius:50%;border:5px solid var(--navy);
    display:flex;align-items:center;justify-content:center;
    font-family:"Questrial",sans-serif;font-size:32px;color:var(--navy)}
  .card--front .logo-mark{left:119px;top:83px}
  .card--back .logo-mark{left:242px;top:77px;width:100px;height:100px;border-color:var(--white);color:var(--white)}

  .brand-name{position:absolute;left:0;width:334px;text-align:center;
    font-family:"Questrial",sans-serif;font-size:31px;color:var(--navy);white-space:nowrap}
  .card--front .brand-name{top:190px}
  .card--back .brand-name{left:0;width:586px;top:186px;color:var(--white)}

  .divider{position:absolute;left:324px;top:58px;width:1px;height:192px;background:var(--rule)}

  .person{position:absolute;left:356px;top:68px;font-family:"Questrial",sans-serif}
  .person__name{font-family:"Montserrat",sans-serif;font-weight:700;font-size:17px;letter-spacing:.3px;color:var(--navy)}
  .person__title{font-size:14px;color:var(--grey-text);margin-top:1px}

  .contacts{position:absolute;left:356px;top:121px;list-style:none;font-family:"Questrial",sans-serif;font-size:13.5px;color:var(--grey-text)}
  .contacts li{display:flex;align-items:center;height:18.7px}
  .contacts .icon{width:13px;height:13px;margin-right:12px;flex:none}

  .address{position:absolute;left:356px;top:207px;font-family:"Questrial",sans-serif;font-size:13.5px;line-height:19px;color:var(--grey-text)}

  .wave{position:absolute;left:0;bottom:0;width:586px;height:60px}

  .website{position:absolute;left:0;width:586px;top:257px;text-align:center;
    font-family:"Questrial",sans-serif;font-size:14px;letter-spacing:.3px;color:var(--white)}
</style>
</head>
<body>
<main class="canvas">

  <section class="card card--front" aria-label="Card front">
    <div class="logo-mark">KoM</div>
    <div class="brand-name">Kestrel of Merit</div>
    <div class="divider"></div>

    <div class="person">
      <div class="person__name">MORGAN HALE</div>
      <div class="person__title">General Manager</div>
    </div>

    <ul class="contacts">
      <li><svg class="icon" viewBox="0 0 13 13"><rect width="13" height="13" rx="2" fill="#0f8fb5"/></svg>/kestrelofmerit</li>
      <li><svg class="icon" viewBox="0 0 13 13"><rect width="13" height="13" rx="2" fill="#0f8fb5"/></svg>/kestrelofmerit</li>
      <li><svg class="icon" viewBox="0 0 13 13"><rect width="13" height="13" rx="2" fill="#0f8fb5"/><path d="M2.5 4h8v5.5h-8z M2.5 4l4 3 4-3" fill="none" stroke="#fff" stroke-width="1"/></svg>hello@kestrelofmerit.com</li>
      <li><svg class="icon" viewBox="0 0 13 13"><rect width="13" height="13" rx="2" fill="#0f8fb5"/><circle cx="6.5" cy="6.5" r="4" fill="none" stroke="#fff" stroke-width="1"/><ellipse cx="6.5" cy="6.5" rx="1.7" ry="4" fill="none" stroke="#fff" stroke-width=".8"/><path d="M2.5 6.5h8" stroke="#fff" stroke-width=".8"/></svg>www.kestrelofmerit.com</li>
    </ul>

    <div class="address">218 Harbor View Lane<br>Clearwater , FL 33755</div>

    <svg class="wave" viewBox="0 0 586 60" preserveAspectRatio="none" aria-hidden="true">
      <path d="M0 38 C130 30 260 8 390 12 C470 15 540 28 586 44 L586 60 L0 60Z" fill="#0f8fb5"/>
      <path d="M140 60 C230 40 320 22 400 22 C470 22 530 36 586 50 L586 60Z" fill="#c9ccd3"/>
      <path d="M190 60 C270 42 340 26 410 25 C470 25 520 40 560 60Z" fill="#141a5c"/>
    </svg>
  </section>

  <section class="card card--back" aria-label="Card back">
    <div class="logo-mark">KoM</div>
    <div class="brand-name">Kestrel of Merit</div>
    <div class="website">www.kestrelofmerit.com</div>
  </section>

</main>
</body>
</html>
```